Flyer Design Project

We are offering a new class on cyber crime and want to advertise this course to students. We would like to see a design that is eye catching and coveys the goals of the course, when it meets and a brief abstract for the class.

The course will focus on the economics of cyber crime so including one or two graphics that get across this point would be good.

Requirements
Must have
• Course name "Cyber Crime"
Call number "CS 795 - 004"
Course meeting time (day of week and time) Tue. 4:30-7:10pm
Course goals
Course abstract

```html
<!DOCTYPE html>
<html lang="en">
<head>
<meta charset="utf-8">
<title>Cyber Crime — CS 795 - 004</title>
<link rel="stylesheet" href="https://fonts.googleapis.com/css2?family=Archivo+Black&family=Jost:wght@400;500;700;800&display=swap">
<style>
  :root {
    --sky: #3aa9dc;
    --navy: #1d3f73;
    --navy-edge: #4f7fb3;
    --white: #ffffff;
    --hero-light: #dfe9f2;
    --hero-mid: #8fb6d6;
    --hero-deep: #2f6fa3;
  }
  * { margin: 0; padding: 0; box-sizing: border-box; }
  html, body { width: 933px; height: 1200px; overflow: hidden; }
  body { background: var(--white); font-family: "Jost", "Futura", sans-serif; color: var(--white); }
  .flyer { position: relative; width: 933px; height: 1200px; overflow: hidden; background: var(--sky); }

  .hero {
    position: absolute; left: 0; top: 0; width: 933px; height: 521px;
    background:
      radial-gradient(ellipse 60% 45% at 55% 22%, rgba(255,255,255,0.85), rgba(255,255,255,0) 70%),
      linear-gradient(180deg, var(--hero-light) 0%, var(--hero-mid) 45%, var(--hero-deep) 75%, var(--hero-mid) 100%);
  }
  .title {
    position: absolute; left: 0; top: 22px; width: 933px; text-align: center;
    font-family: "Archivo Black", "Arial Black", sans-serif;
    font-size: 158px; line-height: 130px; letter-spacing: 2px;
    color: var(--white);
    text-shadow: 4px 5px 8px rgba(20, 50, 90, 0.55);
  }
  .title span { display: block; }

  .details { position: absolute; left: 0; top: 521px; width: 933px; height: 556px; text-align: center; }
  .section-heading { font-weight: 800; font-size: 26px; letter-spacing: 0.5px; line-height: 1; }
  .goals-heading { margin-top: 30px; }
  .goals { list-style: none; margin-top: 14px; font-size: 21.5px; line-height: 26px; }
  .goals li { margin-bottom: 13px; }
  .goals b { font-weight: 800; }
  .abstract-heading { margin-top: 22px; }
  .abstract { margin: 14px auto 0; width: 800px; font-size: 21.5px; line-height: 28px; font-weight: 400; }

  .schedule {
    position: absolute; left: 0; top: 1077px; width: 933px; height: 123px;
    background: var(--navy); border-top: 3px solid var(--navy-edge);
    display: flex; justify-content: space-between; align-items: center;
    padding: 0 26px 6px; font-weight: 800; font-size: 25.5px; letter-spacing: 0.3px;
  }
</style>
</head>
<body>
  <main class="flyer">
    <div class="hero" role="img" aria-label="Blue digital scene of rows of glossy dollar signs under streams of binary code"></div>
    <h1 class="title"><span>CYBER</span><span>CRIME</span></h1>

    <section class="details">
      <h2 class="section-heading goals-heading">COURSE GOALS:</h2>
      <ol class="goals">
        <li><b>1)</b> Understand how modern cyber-crime operates on a<br>technical and economic level</li>
        <li><b>2)</b> Analyze some of the potential places to intervene at an<br>economic, technical and policy level.</li>
      </ol>
      <h2 class="section-heading abstract-heading">COURSE ABSTRACT:</h2>
      <p class="abstract">Arguably the single most significant change in the cyber-security landscape has been the explosive rise of profit-fueled cyber-crime. Obtaining a detailed, structural understanding of how profit-driven cyber crime works — its underlying economics and associated business practices — has the potential to illuminate new defensive measures that might prove far more efficient for countering attacks than purely technical measures. This research seminar will delve into our current understanding of the economics of cyber-crime.</p>
    </section>

    <footer class="schedule">
      <span class="course-number">COURSE: CS 795 - 004</span>
      <span class="course-day">DAY: TUESDAY</span>
      <span class="course-time">TIME: 4:30 PM-7:10PM</span>
    </footer>
  </main>
</body>
</html>
```